Research campaign for the global health issues in Africa must be modern, impactful and unique *

Please see attachment
Research campaign for the global health issues in Africa must be modern, impactful and unique
Updates

Please find the updated flyer requirement. These designs are not modern. We would need this flyer displayed on KD , Pelmora and vexalo. Please use either option of the requirement. Color scheme is Blue.

Target Market(s)

Patients, volunteers, patient advocacy groups, hospitals, healthcare professionals

Industry/Entity Type

Health Care

Font styles to use
Serif

Colors
0355a3
fbed22
f04a50

Requirements
Must have
• Please note that this must be a modern flyer that can be posted on Kandewick so size matters here.
Nice to have
• To see African/black people or foot print or shadow of a walk
• There can be a background image of a child’s face or Person walking or We could have a hand print or foot print with different disease colors.

```html
<!DOCTYPE html>
<html lang="en">
<head>
<meta charset="utf-8">
<title>Walk for Global Health Research Campaign 2019</title>
<link href="https://fonts.googleapis.com/css2?family=Roboto+Condensed:wght@300;400;700&display=swap" rel="stylesheet">
<style>
  :root{
    --navy:#1f2a5c;
    --navy-deep:#141a3f;
    --band-blue:#1d6aa8;
    --teal:#12899a;
    --white:#ffffff;
    --frame:#3f3f8f;
    --photo-blue:#8d9fd0;
    --photo-light:#eef1f8;
    --photo-warm:#f3c7a0;
    --star-edge:#cfe6f2;
  }
  *{margin:0;padding:0;box-sizing:border-box}
  html,body{width:927px;height:1200px;overflow:hidden;background:var(--white)}
  body{font-family:"Roboto Condensed",Arial,sans-serif}
  .flyer{position:relative;width:927px;height:1200px;overflow:hidden;background:var(--white)}
  .lab-photo{position:absolute;left:0;top:0;width:927px;height:900px;
    background:
      radial-gradient(ellipse 260px 340px at 860px 520px,var(--photo-warm),transparent 70%),
      radial-gradient(ellipse 300px 420px at 60px 640px,rgba(60,70,160,.75),transparent 70%),
      radial-gradient(ellipse 420px 260px at 470px 660px,rgba(150,170,215,.7),transparent 75%),
      linear-gradient(180deg,var(--white) 0%,var(--photo-light) 22%,#c9d3ea 55%,var(--photo-blue) 100%);}
  .band{position:absolute;left:0;top:0}
  .kicker{position:absolute;top:78px;left:0;width:927px;text-align:center;font-weight:700;font-size:24px;letter-spacing:18px;color:var(--navy)}
  .kicker-line{position:absolute;top:91px;height:2px;background:var(--navy)}
  .title{position:absolute;top:120px;left:0;width:927px;text-align:center;font-weight:700;font-size:41px;color:var(--navy);letter-spacing:.3px}
  .commemoration{position:absolute;top:192px;left:0;width:927px;text-align:center;font-weight:400;font-size:32px;color:var(--teal)}
  .occasion{position:absolute;top:232px;left:0;width:927px;text-align:center;font-weight:400;font-size:48px;color:var(--teal)}
  .event-card{position:absolute;left:250px;top:330px;width:454px;height:162px;border-radius:16px;background:rgba(255,255,255,.9);text-align:center;color:var(--navy)}
  .event-date{position:absolute;top:24px;width:100%;font-size:33px}
  .event-route{position:absolute;top:72px;width:100%;font-size:16.5px;font-weight:300;color:#2b2b4f}
  .event-time{position:absolute;top:110px;width:100%;font-size:25px}
  .clip{position:absolute;left:274px;top:302px}
  .partners-pill{position:absolute;left:326px;top:586px;width:300px;height:34px;border-radius:17px;background:var(--white);text-align:center;line-height:34px;font-weight:700;font-size:15.5px;color:var(--navy)}
  .partner-slot{position:absolute;top:638px;width:140px;height:73px;border:3px solid var(--frame);border-radius:14px;background:rgba(255,255,255,.35)}
  .brand-tile{position:absolute;left:374px;top:731px;width:170px;height:90px;border-radius:12px;background:rgba(255,255,255,.85);display:flex;align-items:center;justify-content:center;gap:8px}
  .brand-mark{width:14px;height:14px;background:var(--navy)}
  .brand-name{font-weight:700;font-size:19px;color:var(--navy);letter-spacing:.5px}
  .mission{position:absolute;top:828px;left:0;width:927px;text-align:center;font-size:17.5px;line-height:22px;color:#111a33}
  .offer-badge{position:absolute;left:700px;top:760px}
  .benefits-heading{position:absolute;left:68px;top:938px;font-weight:700;font-size:18.5px;color:var(--white)}
  .benefits{position:absolute;left:68px;top:978px;list-style:none;font-size:16px;line-height:20px;color:var(--white);font-weight:300}
  .benefits li::before{content:"•";margin-right:8px}
  .footer-rule{position:absolute;left:30px;top:1083px;width:867px;height:2px;background:linear-gradient(90deg,transparent,#2f6fb0 20%,#2f6fb0 80%,transparent)}
  .contact{position:absolute;top:1100px;font-size:16px;line-height:20px;color:var(--white);font-weight:300}
  .contact strong{font-weight:700}
</style>
</head>
<body>
<main class="flyer">
  <div class="lab-photo" role="img" aria-label="Laboratory scene with glass flasks, sample bottles and a dropper in soft blue and warm light"></div>

  <svg class="band" width="927" height="1200" viewBox="0 0 927 1200" aria-hidden="true">
    <defs>
      <linearGradient id="bandFill" x1="0" y1="0" x2="0" y2="1">
        <stop offset="0" stop-color="#1d6aa8"/>
        <stop offset="0.45" stop-color="#1a3f78"/>
        <stop offset="1" stop-color="#141a3f"/>
      </linearGradient>
    </defs>
    <path d="M0 800 C220 900 600 905 927 845 L927 1200 L0 1200 Z" fill="var(--white)"/>
    <path d="M0 830 C230 920 610 915 927 862 L927 1200 L0 1200 Z" fill="url(#bandFill)"/>
  </svg>

  <div class="kicker-line" style="left:164px;width:156px"></div>
  <div class="kicker">WALK FOR</div>
  <div class="kicker-line" style="left:620px;width:140px"></div>
  <h1 class="title">GLOBAL HEALTH RESEARCH CAMPAIGN 2019</h1>
  <p class="commemoration">IN COMMEMORATION OF</p>
  <h2 class="occasion">THE WORLD CLINICAL TRIALS DAY</h2>

  <section class="event-card">
    <p class="event-date">Saturday, May 25, 2019</p>
    <p class="event-route">Harbor General Gate to Civic Stadium Eastside</p>
    <p class="event-time">7:00 am</p>
  </section>
  <svg class="clip" width="16" height="52" viewBox="0 0 16 52" aria-hidden="true">
    <path d="M4 14 V42 a4 4 0 0 0 8 0 V8 a5 5 0 0 0 -10 0 V38" fill="none" stroke="var(--navy)" stroke-width="2.5" stroke-linecap="round"/>
  </svg>

  <div class="partners-pill">DISEASE FOCUS OF OUR PARTNERS</div>
  <div class="partner-slot" style="left:90px"></div>
  <div class="partner-slot" style="left:244px"></div>
  <div class="partner-slot" style="left:398px"></div>
  <div class="partner-slot" style="left:556px"></div>
  <div class="partner-slot" style="left:710px"></div>

  <div class="brand-tile"><span class="brand-mark"></span><span class="brand-name">NORVALE RESEARCH</span></div>
  <p class="mission">Norvale Research is committed to finding innovative<br>global health solutions through clinical research</p>

  <svg class="offer-badge" width="210" height="210" viewBox="0 0 210 210" aria-label="Free health screening and consultation">
    <polygon fill="var(--navy)" stroke="var(--star-edge)" stroke-width="4" stroke-linejoin="round" points="105,5 115,22 128,8 134,27 150,16 151,36 169,30 165,49 185,48 176,66 195,70 182,85 200,93 184,105 200,117 182,125 195,140 176,144 185,162 165,161 169,180 151,174 150,194 134,183 128,202 115,188 105,205 95,188 82,202 76,183 60,194 59,174 41,180 45,161 25,162 34,144 15,140 28,125 10,117 26,105 10,93 28,85 15,70 34,66 25,48 45,49 41,30 59,36 60,16 76,27 82,8 95,22"/>
    <text x="105" y="88" text-anchor="middle" fill="var(--white)" font-family="Roboto Condensed, sans-serif" font-weight="700" font-size="42">FREE</text>
    <text x="105" y="113" text-anchor="middle" fill="var(--white)" font-family="Roboto Condensed, sans-serif" font-weight="700" font-size="18">HEALTH</text>
    <text x="105" y="135" text-anchor="middle" fill="var(--white)" font-family="Roboto Condensed, sans-serif" font-weight="700" font-size="18">SCREENING AND</text>
    <text x="105" y="157" text-anchor="middle" fill="var(--white)" font-family="Roboto Condensed, sans-serif" font-weight="700" font-size="18">CONSULTATION</text>
  </svg>

  <h3 class="benefits-heading">The potential benefits of participating in a clinical trial may include the following:</h3>
  <ul class="benefits">
    <li>Access to promising new treatments often not available outside the clinical-trial setting</li>
    <li>Treatment that may be more effective than the standard approach</li>
    <li>The opportunity to be the first to benefit from a new method under study</li>
    <li>The chance to play an active role in your own health care and gain a greater understanding of your disease or condition</li>
  </ul>

  <div class="footer-rule"></div>
  <address class="contact" style="left:68px;font-style:normal"><strong>Norvale Research Corporate Office</strong><br>22 Maple Crest Road, Off Bayline Avenue<br>Ikeja, Lagos, Nigeria</address>
  <p class="contact" style="left:384px">Nigeria Office: +23 48100012345<br>International: 1.555.010.2040 (USA)</p>
  <p class="contact" style="left:680px">info@norvaleresearch.com<br>www.norvaleresearch.com</p>
</main>
</body>
</html>
```